Web client portal pref Wordpress

Can this theme be adapted for us?

http://plumcrate.net/item/taskmarlin-job-board-wordpress-theme/48260317?s_phrase=&s_rank=49

We need a web client portal site that a group or individual can log into viewing work that has come in via a lead process. More like a classified listing.
Each lead can be seen by all that log in at any given time. They all can see the description. However, only when they commit to taking the lead can they view the full contact information.
The site would need an admin section that a number of people can be on at the same time, to input the leads. Information needs to be input by admin staff and then viewable by the the clients.
The clients need to be set as to how many leads they can take in a 24hr period.
We will also require a compatible app further down the line.
Here are some further details of what's needed.
1/. Log in cover page. Site can not be viewed unless you are a registered user or admin. There is no sign up facility.
Three buttons: Login , Admin Login and Guest Login

2/. Home Page: Shows Categories and how many leads are in each category.
Lower section to show 5 of the oldest posted leads... These will be called "Featured".
At bottom of page will be links to FAQs page Terms & Conditions and Privacy Policy.

3/. Clicking on a Category: Takes them to all available leads in that category.
The listing shows a description without contact details. Only when they press "Accept" do then see all the info... Name, Address, Email, Home Number and Mobile Number. When the Member clicks Accept a popup comes up with a message to confirm. It says: By clicking confirm you are agreeing to contact the potential client as soon as possible as per your user agreement. This box has a link to User Agreement page and a Cancel and Confirm Button. Only after confirming can they then see all the potential client info. The listing is then removed from general display and a copy placed in their personal account folder.

4/. Lower Admin and Higher Admin.
There are two Admin sections. Lower and Higher. Lower is just able to submit leads in and manages their own individual lead info file.
All access to the site is handled manually by Higher Level Admin that has full view of and manages everything on the site. Higher Level Admin decides how many leads each member gets each day. (24 hr period) Who is added and deleted as members. Ability to suspend a member and reinstate.
All leads need to go into our Zoho CRM at the time of listing. All leads auto deleted from the system after 90 days or manually. All listings showing for max 24 hrs on site with ability to re-list and managed by Lower and Higher Level admin.

Thats it for now, I look forward to you submitting.
There are two other sites to be built after this successful application.
Many thanks

Target Market(s)

UK legal

Industry/Entity Type

Legal

Number of Pages Required

5+ page

Font styles to use
Sans Serif

Requirements
Must have
• As above
Nice to have
• Simple to use clean style. Can only be viewed by members and admin.

```html
<!DOCTYPE html>
<html lang="en">
<head>
<meta charset="utf-8">
<title>Lead Portal</title>
<link rel="stylesheet" href="https://fonts.googleapis.com/css2?family=Open+Sans:wght@400;600;700&display=swap">
<style>
:root{
  --green:#7dbb42;
  --navy:#0d2240;
  --page:#ffffff;
  --header-bg:#f7f7f7;
  --btn-grey:#e4e5e7;
  --btn-border:#cfd1d4;
  --input:#f1f1f1;
  --text:#1a1a1a;
  --muted:#666a70;
  --line:#9a9a9a;
  --news:#5b5b5b;
  --copy:#4a4b4d;
  --strip:#bdbdbd;
}
*{box-sizing:border-box;margin:0;padding:0}
html,body{width:1200px;height:2570px;overflow:hidden}
body{position:relative;background:var(--page);font-family:"Open Sans",Arial,sans-serif;color:var(--text)}
.abs{position:absolute}
a{text-decoration:none}
.site-header{left:0;top:0;width:1200px;height:196px;background:var(--header-bg)}
.logo{left:80px;top:40px;font-size:38px;font-weight:600;color:var(--green)}
.pill{display:flex;align-items:center;justify-content:center;gap:10px;background:var(--btn-grey);border:1px solid var(--btn-border);border-radius:4px;font-size:21px;color:#555}
.pill svg{width:22px;height:26px}
.header-rule{left:80px;top:120px;width:1058px;height:2px;background:#b5b5b5}
.main-nav a{position:absolute;top:143px;font-size:19px;color:#333;letter-spacing:.3px}
.hero{left:0;top:196px;width:1200px;height:663px;background:linear-gradient(100deg,#7b8690 0%,#a7adb2 35%,#6c6e73 60%,#c9ccd0 100%)}
.hero-strip{left:0;top:859px;width:1200px;height:14px;background:var(--strip)}
.field{display:flex;align-items:center;justify-content:space-between;padding:0 22px;background:var(--input);font-size:19px;color:var(--muted)}
.field svg{width:36px;height:36px}
.search-btn{left:1020px;top:745px;width:93px;height:81px;background:var(--green);display:flex;align-items:center;justify-content:center}
.band-left{left:0;top:873px;width:554px;height:176px;background:var(--navy)}
.band-right{left:646px;top:873px;width:554px;height:176px;background:var(--navy)}
.band-gap{left:554px;top:873px;width:92px;height:97px;background:#f3f3f3}
.section-title{font-size:19px;font-weight:600;letter-spacing:.3px}
.cat-grid{left:80px;top:1139px;width:1051px;height:437px;border:1px solid #a8a8a8}
.cat-grid .v{position:absolute;top:0;width:1px;height:100%;background:#a8a8a8}
.cat-grid .h{position:absolute;left:0;top:212px;width:100%;height:1px;background:#a8a8a8}
.category{display:flex;align-items:flex-start;gap:10px;font-size:19px;font-weight:600;color:#3d3d3d;line-height:30px}
.category svg{width:32px;height:32px;flex:none}
.lead-count{display:block;font-size:15px;font-weight:400;color:var(--muted);line-height:22px}
.job-rule{left:81px;width:485px;height:1px;background:var(--line)}
.btn-green{background:var(--green);color:#fff;font-weight:700;display:flex;align-items:center;justify-content:center}
.lead-card{left:753px;top:1714px;width:378px;height:295px;border:1px solid #bdbdbd}
.lead-card h3{position:absolute;left:0;top:10px;width:100%;text-align:center;font-size:20px;font-weight:700}
.lead-meta{position:absolute;left:24px;font-size:19px;font-weight:700;display:flex;align-items:center;gap:10px}
.lead-meta svg{width:16px;height:20px}
.lead-desc{position:absolute;left:24px;top:160px;width:318px;font-family:Arial,sans-serif;font-size:11.5px;line-height:14.5px}
.newsletter{left:0;top:2104px;width:1200px;height:112px;background:var(--news)}
.newsletter h2{position:absolute;left:80px;top:18px;font-size:26px;font-weight:600;color:#fff}
.news-input{left:282px;top:36px;width:546px;height:52px;background:#f1f1f1;font-size:27px;color:#666;padding-left:44px;display:flex;align-items:center}
.news-btn{left:836px;top:36px;width:135px;height:52px;font-size:26px}
.site-footer{left:0;top:2234px;width:1200px;height:282px;background:var(--navy);color:#fff}
.foot-col{position:absolute;top:52px}
.foot-col h4{font-size:19px;font-weight:700;margin-bottom:14px;letter-spacing:.3px}
.foot-col p,.foot-col li{font-family:Arial,sans-serif;font-size:13.5px;line-height:19px;list-style:none}
.copyright{left:0;top:2516px;width:1200px;height:54px;background:var(--copy);color:#fff;font-family:Arial,sans-serif;font-size:14px;font-weight:700;display:flex;align-items:center;justify-content:center}
</style>
</head>
<body>

<header class="site-header abs">
  <div class="logo abs">Logo</div>
  <a class="pill abs" style="left:701px;top:40px;width:175px;height:45px">
    <svg viewBox="0 0 22 26" fill="none" stroke="#555" stroke-width="2"><rect x="2" y="11" width="18" height="13" rx="2"/><path d="M6 11V7a5 5 0 0 1 10 0v4"/></svg>Guest Login</a>
  <a class="pill abs" style="left:909px;top:40px;width:217px;height:45px">
    <svg viewBox="0 0 22 26" fill="none" stroke="#555" stroke-width="2"><circle cx="11" cy="7" r="5"/><path d="M2 25v-5a6 6 0 0 1 6-6h6a6 6 0 0 1 6 6v5z"/></svg>Member Login</a>
  <div class="header-rule abs"></div>
  <nav class="main-nav">
    <a style="left:83px">HOME</a>
    <a style="left:237px">FEATURED LIST</a>
    <a style="left:476px">FOR MEMBERS</a>
    <a style="left:738px">FOR ADMIN</a>
    <a style="left:945px">CATEGORIES</a>
  </nav>
</header>

<div class="hero abs" role="img" aria-label="Photo of three office colleagues reviewing work together at a computer"></div>
<div class="hero-strip abs"></div>

<div class="field abs" style="left:81px;top:745px;width:461px;height:81px">Lead type, Keywords or Reference .....
  <svg viewBox="0 0 36 36" fill="none" stroke="#333" stroke-width="2"><circle cx="18" cy="18" r="15"/><path d="M18 9v9h7"/></svg></div>
<div class="field abs" style="left:559px;top:745px;width:444px;height:81px">City, County, Region .....
  <svg viewBox="0 0 36 36" fill="none" stroke="#333" stroke-width="2"><path d="M18 33s10-11 10-19a10 10 0 0 0-20 0c0 8 10 19 10 19z"/><circle cx="18" cy="14" r="4"/></svg></div>
<div class="search-btn abs">
  <svg width="42" height="42" viewBox="0 0 42 42" fill="none" stroke="#fff" stroke-width="3"><circle cx="17" cy="17" r="13"/><path d="M27 27l12 12"/></svg></div>

<div class="band-left abs"></div>
<div class="band-gap abs"></div>
<div class="band-right abs"></div>
<div class="field abs" style="left:81px;top:921px;width:442px;height:82px">Search by categories .....
  <svg viewBox="0 0 36 36" fill="none" stroke="#333" stroke-width="2"><circle cx="15" cy="15" r="11"/><path d="M23 23l11 11"/></svg></div>
<a class="pill abs" style="left:679px;top:937px;width:216px;height:47px">
  <svg viewBox="0 0 22 26" fill="none" stroke="#555" stroke-width="2"><rect x="2" y="11" width="18" height="13" rx="2"/><path d="M6 11V7a5 5 0 0 1 10 0v4"/></svg>Admin Login</a>
<a class="pill abs" style="left:913px;top:937px;width:216px;height:47px">
  <svg viewBox="0 0 22 26" fill="none" stroke="#555" stroke-width="2"><rect x="2" y="11" width="18" height="13" rx="2"/><path d="M6 11V7a5 5 0 0 1 10 0v4"/></svg>Client Login</a>

<h2 class="section-title abs" style="left:81px;top:1081px">POPULAR CATEGORIES</h2>
<div class="cat-grid abs">
  <div class="v" style="left:251px"></div><div class="v" style="left:524px"></div><div class="v" style="left:808px"></div>
  <div class="h"></div>
</div>
<svg width="0" height="0" style="position:absolute">
  <defs>
    <g id="ico-clock" fill="none" stroke="#7dbb42" stroke-width="2.4"><circle cx="17" cy="17" r="14"/><path d="M17 9v8l6 4"/></g>
  </defs>
</svg>
<div class="category abs" style="left:88px;top:1160px"><svg viewBox="0 0 34 34" fill="none" stroke="#7dbb42" stroke-width="2.4"><circle cx="17" cy="17" r="14"/><path d="M23 11l-4 8-8 4 4-8z"/></svg><div>Travel &amp; Transport<span class="lead-count">14 leads</span></div></div>
<div class="category abs" style="left:360px;top:1160px"><svg viewBox="0 0 34 34" fill="none" stroke="#7dbb42" stroke-width="2.4"><path d="M3 17L17 5l14 12"/><path d="M7 14v16h20V14"/><path d="M14 30v-9h6v9"/></svg><div>Shopping Centre<span class="lead-count">9 leads</span></div></div>
<div class="category abs" style="left:673px;top:1160px"><svg viewBox="0 0 34 34"><use href="#ico-clock"/></svg><div>Life Care<span class="lead-count">21 leads</span></div></div>
<div class="category abs" style="left:920px;top:1152px"><svg viewBox="0 0 34 50" style="height:46px" fill="#7dbb42"><path d="M17 48S3 28 3 17a14 14 0 0 1 28 0c0 11-14 31-14 31z"/><circle cx="17" cy="16" r="5" fill="#fff"/></svg><div style="padding-top:8px">Travel Agency<span class="lead-count">6 leads</span></div></div>
<div class="category abs" style="left:107px;top:1390px"><svg viewBox="0 0 34 34"><use href="#ico-clock"/></svg><div>Sport Centre<span class="lead-count">11 leads</span></div></div>
<div class="category abs" style="left:369px;top:1388px"><svg viewBox="0 0 34 34" fill="none" stroke="#7dbb42" stroke-width="2.4"><rect x="2" y="8" width="30" height="22" rx="2"/><circle cx="17" cy="19" r="6"/><path d="M11 8l3-4h6l3 4"/></svg><div>Entertainment<span class="lead-count">8 leads</span></div></div>
<div class="category abs" style="left:636px;top:1384px"><svg viewBox="0 0 50 34" style="width:48px" fill="none" stroke="#7dbb42" stroke-width="2.4"><path d="M2 6h28v20H2zM30 13h10l7 7v6H30z"/><circle cx="10" cy="28" r="4" fill="#fff"/><circle cx="22" cy="28" r="4" fill="#fff"/><circle cx="40" cy="28" r="4" fill="#fff"/></svg><div>Car Show Rooms<span class="lead-count">5 leads</span></div></div>
<div class="category abs" style="left:897px;top:1378px"><svg viewBox="0 0 50 44" style="width:46px;height:40px" fill="none" stroke="#7dbb42" stroke-width="2.4"><path d="M2 4h8l6 26h26l5-18H12"/><circle cx="19" cy="38" r="3"/><circle cx="39" cy="38" r="3"/></svg><div>Retails Shopping<span class="lead-count">12 leads</span></div></div>

<h2 class="section-title abs" style="left:81px;top:1649px">RECENT LEADS</h2>
<h2 class="section-title abs" style="left:900px;top:1649px">FEATURED LEADS &nbsp;&lt; &nbsp;&gt;</h2>
<div class="job-rule abs" style="top:1714px"></div>
<div class="job-rule abs" style="top:1860px"></div>
<div class="job-rule abs" style="top:2007px"></div>
<a class="btn-green abs" style="left:244px;top:2036px;width:175px;height:33px;font-size:13px">SHOW MORE LEADS</a>

<article class="lead-card abs">
  <h3>CONVEYANCING</h3>
  <div class="lead-meta" style="top:42px">Brightmoor</div>
  <div class="lead-meta" style="top:71px">Leeds <svg viewBox="0 0 16 20" fill="none" stroke="#555" stroke-width="1.8"><path d="M8 19S2 12 2 7a6 6 0 0 1 12 0c0 5-6 12-6 12z"/><circle cx="8" cy="7" r="2"/></svg></div>
  <div class="lead-meta" style="top:101px">Residential <svg viewBox="0 0 18 18" fill="none" stroke="#555" stroke-width="1.6"><circle cx="9" cy="10" r="6"/><path d="M9 7v3h2M2 4l3-2M16 4l-3-2"/></svg></div>
  <div class="lead-meta" style="top:130px">1,200 <span style="margin-left:22px;font-size:18px">£</span></div>
  <p class="lead-desc">Lorem ipsum dolor sit amet, consectetuer adipiscing elit. Aenean commodo ligula eget dolor. Aenean massa. Cum sociis natoque penatibus et magnis dis parturient montes, nascetur ridiculus mus. Donec quam felis, ultricies nec, pellentesque eu, pretium quis, sem.</p>
  <a class="btn-green abs" style="left:112px;top:252px;width:174px;height:34px;font-size:13px">ACCEPT THIS LEAD</a>
</article>

<section class="newsletter abs">
  <h2>NEWSLETTER</h2>
  <div class="news-input abs">E mail address</div>
  <a class="btn-green news-btn abs">SIGNUP</a>
</section>

<footer class="site-footer abs">
  <div class="foot-col" style="left:81px;width:205px">
    <h4>ABOUT US</h4>
    <p>Lorem ipsum dolor sit amet, consectetuer adipiscing elit. Aenean commodo ligula eget dolor. Aenean massa. Cum sociis natoque penatibus et magnis dis parturient montes, nascetur ridiculus mus. Donec quam felis, ultricies nec, pellentesque eu, pretium quis, sem.</p>
  </div>
  <div class="foot-col" style="left:362px">
    <h4>PRIVACY POLICY</h4>
    <ul><li>&gt; Lorem ipsum dolor sit amet,</li><li>&gt; Lorem ipsum dolor sit amet,</li><li>&gt; Lorem ipsum dolor sit amet,</li><li>&gt; Lorem ipsum dolor sit amet,</li></ul>
  </div>
  <div class="foot-col" style="left:627px;width:205px">
    <h4>TERM &amp; CONDITIONS</h4>
    <p>Lorem ipsum dolor sit amet, consectetuer adipiscing elit. Aenean commodo ligula eget dolor. Aenean massa. Cum sociis natoque penatibus et magnis dis parturient montes, nascetur ridiculus mus. Donec quam felis, ultricies nec, pellentesque eu, pretium quis, sem.</p>
  </div>
  <div class="foot-col" style="left:911px">
    <h4 style="padding-left:52px">FAQ’S</h4>
    <ul><li>&gt; Lorem ipsum dolor sit amet,</li><li>&gt; Lorem ipsum dolor sit amet,</li><li>&gt; Lorem ipsum dolor sit amet,</li><li>&gt; Lorem ipsum dolor sit amet,</li></ul>
  </div>
</footer>
<div class="copyright abs">Copyright 2016 - @ Company Name</div>

</body>
</html>
```